Photography and Political Commentary Blog

Hi there!
I'd like to build a clean, simple, yet visually appealing blog using a theme similar to this: http://www.brightlayouts.net/demo/?theme=TheFrame. I’m looking to work with a designer who has a modern aesthetic who can work with me to create a great blog. Hopefully that’s you!
Details:
The aim would be for the blog to be simple and clean, with each post represented by a picture, title and short summary as with ‘The Frame’ theme. These post summaries would be displayed in a single area without sidebars or columns.
There would be a home page in addition to four pages that you can access from a menu panel. These subordinate pages would be very similar if not the same in style to the main page. The subordinate pages would be:
- Politics
- Security
- Photography
- Music
For each page:
Politics and Security. These pages would be in a traditional blog format with the ability to post, hyperlink, comment etc. Posts would typically be 200-400 words. I am in the military and actively involved in politics and would like to be able to post my thoughts on issues ‘Quick Thoughts on Big Ideas’, and hyperlink to articles with short personal comments.
Photography. The photography main page would be like the homepage with each post represented by a single photo, title and summary (as per ‘The Frame’ theme). The individual posts would need to be able to display photo galleries in a grid, with the ability to click on individual photos to view them in high definition. I am open to the use of different widgets to best display the photos. Typically, each gallery would have 6-10 photos. I am a keen amateur (semi-professional?) photographer. This page would showcase small galleries of my artistic work as opposed to large journal/travel style galleries.
Music. This page is a simply way for me to post links to songs I like from ClipNest, Reelo, Tunebarn etc.
I like the clean style and typeface of the following blogs:
http://www.gallowmark.com/
http://www.thecusp.com/
http://quenlatori.com/
http://hollyonstuffs.com/
http://whatmysisterpicked.jotpage.com/
I like color palates similar to these –
http://www.huevault.com/palette/482137/Moss_Heron
http://www.huevault.com/palette/2958/Cedar_Nine
The first file I have attached is a logo that uses the types of colors and look I'd like to achieve. The second file I have attached has the type of font I'd like to use (something in the 'Sans' family: http://www.typecrate.com/fonts/category/sans/
In general, I like the use of red highlights with other neutral tones (greys, blues etc) but I’m open to your ideas!
For the function of the blog, the homepage would be a sequential summary of the posts from each of the subsections (politics, security, photography and music). I'd like this to be grouped so you can see 3 or 4 of the most recent posts from each section - but I'm open to ideas. The main pages for each subsection would be the same: a sequential summary of the posts for that area. If using Wordpress, I would like to be able to do this automatically, for instance by allocating ‘categories’ to each post that sort the posts into their respective sections.
The site name will be gavinmarsh.com.au. Any logos or headings would be my name ‘Gavin Marsh’. I already own the domain name.
The main aim for this project is for it to be clean, simple and elegant (in a modern way). Something that people can open and easily navigate without clutter, yet is visually appealing.
Thanks for taking the time to read this brief and really looking forward to working with you!
Cheers!
Gav

```html
<!DOCTYPE html>
<html lang="en">
<head>
<meta charset="utf-8">
<title>Gavin Marsh</title>
<link rel="stylesheet" href="https://fonts.googleapis.com/css2?family=Fjalla+One&display=swap">
<style>
:root{
  --brown:#614537;
  --teal:#0d9bac;
  --orange:#ec6a3d;
  --yellow:#efc94f;
  --red:#d03340;
  --white:#ffffff;
  --grey:#6a6a6a;
  --head:"Fjalla One", Arial, sans-serif;
  --body:Arial, Helvetica, sans-serif;
}
*{margin:0;padding:0;box-sizing:border-box}
html,body{width:1200px;height:2466px;overflow:hidden;background:var(--brown)}
.page{position:relative;width:1200px;height:2466px;background:var(--brown)}
.masthead{position:absolute;left:0;top:0;width:1200px;height:148px}
.brand{position:absolute;left:41px;top:22px;font-family:var(--head);font-size:82px;line-height:100px;color:var(--teal);display:flex;align-items:center;gap:20px}
.brand-dot{width:56px;height:56px;border-radius:50%;background:var(--yellow)}
.social{position:absolute;display:flex;gap:17px}
.social span{display:block;width:53px;height:53px;border-radius:50%}
.masthead .social{left:836px;top:54px}
.masthead .social span{background:var(--teal)}
.nav{position:absolute;left:0;top:151px;width:1200px;height:55px;background:var(--orange)}
.nav a{position:absolute;top:11px;font-family:var(--head);font-size:29px;line-height:34px;color:var(--yellow);text-decoration:none}
.nav a.current{color:var(--white)}
.search{position:absolute;left:834px;top:7px;width:346px;height:42px;background:var(--yellow);display:flex;align-items:center}
.search span{font-family:var(--head);font-size:24px;color:var(--brown);padding-left:14px;flex:1}
.search svg{border-left:2px solid #c9a43a;height:30px;width:50px;padding:0 10px}
.section{position:absolute;left:15px;width:1165px;height:471px;background:var(--white)}
.section-label{position:absolute;left:0;top:26px;width:261px;height:48px;font-family:var(--head);font-size:36px;line-height:48px;color:var(--white);padding-left:31px}
.card{position:absolute;top:100px;width:323px}
.card-photo{display:block;width:323px;height:217px;border:5px solid var(--brown)}
.card-title{margin-top:10px;font-family:var(--head);font-size:23px;line-height:30px;color:var(--brown);font-weight:400;white-space:nowrap}
.card-text{margin-top:2px;font-family:var(--body);font-size:14.5px;line-height:17.6px;color:var(--grey)}
.footer{position:absolute;left:0;top:2186px;width:1200px;height:280px;background:var(--teal);color:var(--white);font-family:var(--body)}
.newsletter{position:absolute;left:33px;top:38px;width:600px}
.newsletter h3{font-size:20px;font-weight:400}
.newsletter h3 b{font-weight:700}
.newsletter p{margin-top:8px;font-size:13.5px;line-height:17px;font-weight:700}
.signup{position:absolute;left:30px;top:116px;display:flex;gap:16px}
.signup .field{width:460px;height:40px;border:2px solid var(--yellow)}
.signup .button{width:136px;height:40px;background:var(--yellow);color:var(--brown);font-size:19px;line-height:40px;text-align:center}
.location{position:absolute;left:814px;top:38px}
.location h3{font-size:20px;font-weight:400}
.location p{margin-top:8px;font-size:13.5px;line-height:17px;font-weight:700}
.footer .social{left:810px;top:142px}
.footer .social span{background:var(--yellow)}
.rule{position:absolute;left:0;top:213px;width:1200px;height:2px;background:rgba(255,255,255,.35)}
.footer-links{position:absolute;left:31px;top:233px;display:flex;gap:20px;font-size:14.5px}
.footer-links .current{color:var(--yellow)}
.copyright{position:absolute;left:814px;top:233px;font-size:13.5px}
</style>
</head>
<body>
<div class="page">
  <header class="masthead">
    <div class="brand"><span class="brand-dot"></span><span>Gavin Marsh</span></div>
    <div class="social" aria-label="Social links"><span></span><span></span><span></span><span></span><span></span></div>
  </header>

  <nav class="nav">
    <a class="current" style="left:41px" href="#">HOME</a>
    <a style="left:168px" href="#">PHOTOGRAPHY</a>
    <a style="left:390px" href="#">POLITICS</a>
    <a style="left:549px" href="#">SECURITY</a>
    <a style="left:717px" href="#">MUSIC</a>
    <div class="search"><span>search</span>
      <svg viewBox="0 0 30 30"><circle cx="12" cy="12" r="7" fill="none" stroke="#614537" stroke-width="3"/><line x1="17" y1="17" x2="26" y2="26" stroke="#614537" stroke-width="4" stroke-linecap="round"/></svg>
    </div>
  </nav>

  <section class="section" style="top:225px">
    <h2 class="section-label" style="background:var(--teal)">PHOTOGRAPHY</h2>
    <article class="card" style="left:38px"><div class="card-photo" role="img" aria-label="Underwater portrait photograph" style="background:linear-gradient(160deg,#4fc6c0,#2a7f86 55%,#1e4e55)"></div><h3 class="card-title">Street Musicians in Black and White</h3><p class="card-text">I have been more interested with photography since I got a new camera. It's always exciting to capture moments, walk on the streets and find great subjects. I am also always look for</p></article>
    <article class="card" style="left:416px"><div class="card-photo" role="img" aria-label="Photograph of a multicoloured rose in snow" style="background:radial-gradient(circle at 55% 45%,#c0506a,#4a78a8 35%,#5a6470 70%,#c8ccd2)"></div><h3 class="card-title">Daily Inspiration Colorful Flower</h3><p class="card-text">This post is part of our daily series of posts showing the most inspiring images selected by some of the Quenlatori's writers and users. If you want to participate and share your graphic design</p></article>
    <article class="card" style="left:795px"><div class="card-photo" role="img" aria-label="Photograph of a vintage turquoise car on a street" style="background:linear-gradient(180deg,#b9c3c8,#8a8b80 45%,#5fb8b4 70%,#6c6a5e)"></div><h3 class="card-title">Playwell brings a clean new look to ...</h3><p class="card-text">Editors and contributors share their thoughts on the national pavilions at the Lindmoor Biennial and 'The Lantern Archive' curated by Teodor Alvane.</p></article>
  </section>

  <section class="section" style="top:717px">
    <h2 class="section-label" style="background:var(--yellow)">POLITICS</h2>
    <article class="card" style="left:38px"><div class="card-photo" role="img" aria-label="Black and white photograph of a newspaper reader" style="background:linear-gradient(180deg,#2a2a2a,#9a9a9a 50%,#d8d8d8)"></div><h3 class="card-title">Street Musicians in Black and White</h3><p class="card-text">I have been more interested with photography since I got a new camera. It's always exciting to capture moments, walk on the streets and find great subjects. I am also always look for</p></article>
    <article class="card" style="left:416px"><div class="card-photo" role="img" aria-label="Photograph of two costumed figures" style="background:linear-gradient(180deg,#b8b2ac,#8a7a68 55%,#4e4536)"></div><h3 class="card-title">Daily Inspiration Colorful Flower</h3><p class="card-text">This post is part of our daily series of posts showing the most inspiring images selected by some of the Quenlatori's writers and users. If you want to participate and share your graphic design</p></article>
    <article class="card" style="left:795px"><div class="card-photo" role="img" aria-label="Photograph of a street with protest signs" style="background:linear-gradient(180deg,#c9cfd6,#b49a7c 45%,#7c7064)"></div><h3 class="card-title">Playwell brings a clean new look to ...</h3><p class="card-text">Editors and contributors share their thoughts on the national pavilions at the Lindmoor Biennial and 'The Lantern Archive' curated by Teodor Alvane.</p></article>
  </section>

  <section class="section" style="top:1207px">
    <h2 class="section-label" style="background:var(--orange)">SECURITY</h2>
    <article class="card" style="left:38px"><div class="card-photo" role="img" aria-label="Photograph of a soldier overlooking a town" style="background:linear-gradient(180deg,#dfe3e6,#9a9088 50%,#6e5e4c)"></div><h3 class="card-title">Street Musicians in Black and White</h3><p class="card-text">I have been more interested with photography since I got a new camera. It's always exciting to capture moments, walk on the streets and find great subjects. I am also always look for</p></article>
    <article class="card" style="left:416px"><div class="card-photo" role="img" aria-label="Close photograph of a door lock" style="background:radial-gradient(circle at 60% 50%,#cfc8b4,#9aa8b8 40%,#6a88ae)"></div><h3 class="card-title">Daily Inspiration Colorful Flower</h3><p class="card-text">This post is part of our daily series of posts showing the most inspiring images selected by some of the Quenlatori's writers and users. If you want to participate and share your graphic design</p></article>
    <article class="card" style="left:795px"><div class="card-photo" role="img" aria-label="High contrast action photograph" style="background:linear-gradient(135deg,#111,#8a8a90 45%,#f2f2f2 60%,#222)"></div><h3 class="card-title">Playwell brings a clean new look to ...</h3><p class="card-text">Editors and contributors share their thoughts on the national pavilions at the Lindmoor Biennial and 'The Lantern Archive' curated by Teodor Alvane.</p></article>
  </section>

  <section class="section" style="top:1697px">
    <h2 class="section-label" style="background:var(--red)">MUSIC</h2>
    <article class="card" style="left:38px"><div class="card-photo" role="img" aria-label="Photograph of a singer in a jungle setting" style="background:linear-gradient(180deg,#7fae4a,#4e7a2c 50%,#a8c070)"></div><h3 class="card-title">Lena Voss - Ember</h3><p class="card-text">I have been more interested with photography since I got a new camera. It's always exciting to capture moments, walk on the streets and find great subjects. I am also always look for</p></article>
    <article class="card" style="left:416px"><div class="card-photo" role="img" aria-label="Photograph of a performer on a large metal ball" style="background:linear-gradient(180deg,#5a5a5a,#9a9a98 50%,#6a6a68)"></div><h3 class="card-title">Rae Calloway - Iron Swing</h3><p class="card-text">This post is part of our daily series of posts showing the most inspiring images selected by some of the Quenlatori's writers and users. If you want to participate and share your graphic design</p></article>
    <article class="card" style="left:795px"><div class="card-photo" role="img" aria-label="Photograph of a band standing outdoors" style="background:linear-gradient(180deg,#e8e6dc,#8a8678 45%,#3a3630)"></div><h3 class="card-title">NORTHBOUND LIGHTS - Long Road</h3><p class="card-text">Editors and contributors share their thoughts on the national pavilions at the Lindmoor Biennial and 'The Lantern Archive' curated by Teodor Alvane.</p></article>
  </section>

  <footer class="footer">
    <div class="newsletter">
      <h3><b>Subscribe</b> to our newsletter</h3>
      <p>At vero eos et accusamus et iusto odio dignissimos ducimus, qui blanditiis praesentium voluptatum deleniti atque corrupti, quos dolores et quas molestias excepturi sint."</p>
    </div>
    <div class="signup"><div class="field"></div><div class="button">Notify me</div></div>
    <div class="location">
      <h3>Our location</h3>
      <p>412 Kelvin Row<br>Brindle, K12 7QT<br>Phone: +1 555 014 2290</p>
    </div>
    <div class="social" aria-label="Social links"><span></span><span></span><span></span><span></span><span></span></div>
    <div class="rule"></div>
    <div class="footer-links"><span class="current">Home</span><span>Photograpy</span><span>Politics</span><span>Security</span><span>Music</span></div>
    <div class="copyright"><b>Gavin Marsh</b> © 2013. All Rights Reserved</div>
  </footer>
</div>
</body>
</html>
```